Corvane Summit

Need very crisp business cards for Corvane Summit per the logo attached. The vision of Corvane Summit is 'Guide every Venture to Corvane'. I am going into Freelance | Consulting | Contracting and need this communicated on the card. I need the card to provide a clear message of professionalism and what the vision emulates. Will need an area for my website, LinkedIn, Twitter, as fell as the obvious Name, Address, phone, email... on the back, I would like the Vision but receptive to your design ideas.

```html
<!DOCTYPE html>
<html lang="en">
<head>
<meta charset="utf-8">
<title>Corvane Summit — Business Card</title>
<link rel="stylesheet" href="https://fonts.googleapis.com/css2?family=Montserrat:wght@500;600&family=Arimo:wght@400&family=Tinos:wght@700&display=swap">
<style>
  :root {
    --navy: #233871;
    --ink: #2b2b2b;
    --grey: #555a63;
    --paper: #ffffff;
    --backdrop: #e4e1de;
  }
  * { margin: 0; padding: 0; box-sizing: border-box; }
  html, body { width: 1200px; height: 960px; overflow: hidden; }
  body {
    background: var(--backdrop);
    display: flex;
    flex-direction: column;
    align-items: center;
    justify-content: center;
    gap: 30px;
  }
  .card {
    position: relative;
    width: 770px;
    height: 440px;
    overflow: hidden;
    box-shadow: 0 6px 18px rgba(0,0,0,0.12);
  }

  /* Brand lockup: name + vision tagline */
  .brand {
    display: flex;
    align-items: center;
    font-family: "Montserrat", sans-serif;
  }
  .brand__mark { flex: none; }
  .brand__text { display: flex; flex-direction: column; }
  .brand__name { font-weight: 600; letter-spacing: -0.5px; line-height: 1.05; }
  .brand__vision {
    font-weight: 500;
    text-transform: uppercase;
    white-space: nowrap;
  }

  /* Front */
  .card--front {
    background: var(--navy);
    display: flex;
    flex-direction: column;
    align-items: center;
    justify-content: center;
    gap: 44px;
  }
  .card--front .brand { gap: 18px; color: var(--paper); }
  .card--front .brand__mark { width: 56px; height: 56px; border-radius: 6px; background: var(--paper); }
  .card--front .brand__name { font-size: 52px; }
  .card--front .brand__vision { font-size: 12px; letter-spacing: 4.2px; margin-top: 6px; }
  .services {
    font-family: "Arimo", sans-serif;
    font-size: 15px;
    letter-spacing: 2px;
    text-transform: uppercase;
    color: var(--paper);
    opacity: 0.85;
  }

  /* Back */
  .card--back { background: var(--paper); }
  .card--back .brand {
    position: absolute;
    left: 60px;
    top: 92px;
    gap: 12px;
    color: var(--navy);
  }
  .card--back .brand__mark { width: 34px; height: 34px; border-radius: 4px; background: var(--navy); }
  .card--back .brand__name { font-size: 32px; }
  .card--back .brand__vision { font-size: 8px; letter-spacing: 2.6px; margin-top: 4px; color: var(--grey); }

  .person {
    position: absolute;
    right: 50px;
    top: 76px;
    text-align: right;
  }
  .person__name {
    font-family: "Tinos", serif;
    font-weight: 700;
    font-size: 32px;
    color: var(--navy);
  }
  .person__role {
    font-family: "Arimo", sans-serif;
    font-size: 17px;
    color: var(--grey);
    margin-top: 2px;
  }
  .person__services {
    font-family: "Arimo", sans-serif;
    font-size: 12px;
    letter-spacing: 0.5px;
    color: var(--grey);
    margin-top: 4px;
  }
  .divider {
    position: absolute;
    left: 130px;
    right: 40px;
    top: 186px;
    height: 2px;
    background: var(--navy);
  }
  .address {
    position: absolute;
    right: 50px;
    top: 214px;
    text-align: right;
    font-family: "Arimo", sans-serif;
    font-size: 19px;
    line-height: 1.3;
    color: var(--ink);
  }
  .contacts {
    position: absolute;
    left: 150px;
    top: 210px;
    list-style: none;
    font-family: "Arimo", sans-serif;
    font-size: 20px;
    color: var(--ink);
  }
  .contacts li { display: flex; align-items: center; gap: 14px; line-height: 34px; }
  .contacts svg { width: 16px; height: 16px; fill: var(--navy); flex: none; }
  .wave { position: absolute; left: 0; top: 0; }
  .social {
    position: absolute;
    right: 36px;
    top: 380px;
    display: flex;
    align-items: center;
    gap: 8px;
    font-family: "Arimo", sans-serif;
    font-size: 19px;
    color: var(--paper);
  }
  .social__dot { width: 14px; height: 14px; border-radius: 50%; background: var(--paper); }
</style>
</head>
<body>
  <section class="card card--front" aria-label="Card front">
    <div class="brand">
      <span class="brand__mark"></span>
      <span class="brand__text">
        <span class="brand__name">Corvane Summit</span>
        <span class="brand__vision">Guide every Venture to Corvane</span>
      </span>
    </div>
    <p class="services">Freelance | Consulting | Contracting</p>
  </section>

  <section class="card card--back" aria-label="Card back">
    <svg class="wave" width="770" height="440" viewBox="0 0 770 440" aria-hidden="true">
      <path d="M0 400 L430 400" stroke="var(--ink)" stroke-width="6" fill="none"/>
      <path d="M0 412 L440 412 C505 412 510 358 575 356 L770 356 L770 440 L0 440 Z" fill="var(--navy)"/>
    </svg>

    <div class="brand">
      <span class="brand__mark"></span>
      <span class="brand__text">
        <span class="brand__name">Corvane Summit</span>
        <span class="brand__vision">Guide every Venture to Corvane</span>
      </span>
    </div>

    <div class="person">
      <div class="person__name">Daniel Harrow</div>
      <div class="person__role">Owner</div>
      <div class="person__services">Freelance | Consulting | Contracting</div>
    </div>

    <div class="divider"></div>

    <div class="address">1480 Ridgeway Rd. Elmford<br>AR 70000</div>

    <ul class="contacts">
      <li><svg viewBox="0 0 16 16"><path d="M3 1h3l1.5 4-2 1.3a8 8 0 0 0 4.2 4.2L11 8.5l4 1.5v3a2 2 0 0 1-2 2A12 12 0 0 1 1 3a2 2 0 0 1 2-2z"/></svg>555-214-0386</li>
      <li><svg viewBox="0 0 16 16"><path d="M1 3h14v10H1z M2 4v.4l6 4.2 6-4.2V4z" fill-rule="evenodd"/></svg>info@corvanesummit.com</li>
      <li><svg viewBox="0 0 16 16"><circle cx="8" cy="8" r="7"/></svg>www.corvanesummit.com</li>
    </ul>

    <div class="social">@corvanesummit <span class="social__dot"></span><span class="social__dot"></span></div>
  </section>
</body>
</html>
```